Psychology text book for statistics needs front cover

We need a logo/picture that will be the front cover of our book.

Our book is on person-specific data analysis. Such as: predicting when someone might binge drink, understanding personal processes (e.g., emotional processes; brain processes), or quantifying what depression means for a given individual.

So, something that merges the concept of people as individuals with their own processes (or life path) with statistics would be great.

Target Market(s)

Higher education

Logo Text

Patterns Within One Life (optional)

Logo styles of interest
Pictorial/Combination Logo
Abstract Logo
Font styles to use
Sans Serif

Requirements
Must have
• The title of the book is:
Patterns Within One Life: Dynamic Methods for Personal Change Modeling

It would be fine to just include the first part - Patterns Within One Life
Nice to have
• For inspiration: perhaps something that has a clear image of an individual in a crowd where everyone else is blurry. Or on a path. If you could figure out how to meld this together with some image representing data across time (such as lines on a plot see examples), that would be great.

```html
<!DOCTYPE html>
<html lang="en">
<head>
<meta charset="utf-8">
<title>Patterns Within One Life — Book Cover</title>
<link rel="stylesheet" href="https://fonts.googleapis.com/css2?family=Bebas+Neue&family=Montserrat:wght@500;700&display=swap">
<style>
  :root {
    --page: #ffffff;
    --cover-yellow: #fad10a;
    --accent-red: #e8202a;
    --title-black: #0a0a0a;
    --title-blue: #1b4c9a;
    --band-black: #000000;
    --author-white: #ffffff;
  }
  * { margin: 0; padding: 0; box-sizing: border-box; }
  html, body {
    width: 1200px;
    height: 1200px;
    overflow: hidden;
    background: var(--page);
  }
  .canvas {
    position: relative;
    width: 1200px;
    height: 1200px;
    background: var(--page);
  }
  .book-cover {
    position: absolute;
    left: 360px;
    top: 240px;
    width: 480px;
    height: 720px;
    background: var(--cover-yellow);
    overflow: hidden;
  }
  .title-block {
    position: absolute;
    left: 0;
    top: 0;
    width: 480px;
    height: 369px;
  }
  .accent-bar {
    position: absolute;
    left: 29px;
    top: 32px;
    width: 20px;
    height: 337px;
    background: var(--accent-red);
  }
  .book-title {
    position: absolute;
    left: 64px;
    top: 20px;
    font-family: "Bebas Neue", "Oswald", sans-serif;
    font-weight: 400;
    font-size: 111px;
    line-height: 80px;
    letter-spacing: 1px;
    text-transform: uppercase;
  }
  .book-title span { display: block; }
  .title-dark { color: var(--title-black); }
  .title-blue { color: var(--title-blue); }
  .cover-photo {
    position: absolute;
    left: 0;
    top: 369px;
    width: 480px;
    height: 230px;
    background:
      linear-gradient(120deg, rgba(250,209,10,0.35) 0%, rgba(250,209,10,0) 40%, rgba(250,209,10,0.3) 75%, rgba(250,209,10,0.1) 100%),
      linear-gradient(180deg, #a8a39a 0%, #8d8a84 50%, #b3aea3 100%);
  }
  .subtitle-band {
    position: absolute;
    left: 0;
    top: 599px;
    width: 480px;
    height: 68px;
    display: flex;
    align-items: center;
    justify-content: center;
    text-align: center;
  }
  .book-subtitle {
    font-family: "Montserrat", sans-serif;
    font-weight: 700;
    font-size: 18px;
    line-height: 22px;
    letter-spacing: 3px;
    color: var(--accent-red);
    text-transform: uppercase;
  }
  .author-band {
    position: absolute;
    left: 0;
    top: 667px;
    width: 480px;
    height: 53px;
    background: var(--band-black);
    display: flex;
    align-items: center;
    justify-content: center;
  }
  .author-names {
    font-family: "Montserrat", sans-serif;
    font-weight: 500;
    font-size: 18px;
    letter-spacing: 3px;
    color: var(--author-white);
    text-transform: uppercase;
  }
</style>
</head>
<body>
  <main class="canvas">
    <section class="book-cover">
      <header class="title-block">
        <div class="accent-bar"></div>
        <h1 class="book-title">
          <span class="title-dark">Patterns</span>
          <span class="title-dark">Within</span>
          <span class="title-blue">One</span>
          <span class="title-blue">Life</span>
        </h1>
      </header>
      <div class="cover-photo" role="img" aria-label="Overhead photo of a crowd blurred in motion on a yellow-striped crosswalk, with one woman standing still and sharp in the centre"></div>
      <div class="subtitle-band">
        <p class="book-subtitle">Dynamic Methods for<br>Personal Change Modeling</p>
      </div>
      <footer class="author-band">
        <p class="author-names">Author Names</p>
      </footer>
    </section>
  </main>
</body>
</html>
```